Fun Language School in San Diego, CA - We want cool Business Card

We need a new business card design for our new logo. We are a language school in beautiful San Diego, California. Our target is students from all over the world who age from 18 to 25. They come to our school to learn English. Our school has a modern look, trending and fun place. We are the only language school who use tablets in class. We are student oriented, Students Come First is our slogan. We are re-branding ourselves with a new logo. We would like to see a designs that use our new logo and it should reflect the feel of young, fun, modern, high-tech and attractive to young people.
I've seen some business card designs with transparent look, unusual shapes, we are open to any cool ideas. Thank you very much!

In order for you to know more about our school, here are the links to our Youtube Channel and Facebook.

Youtube: https://www.vidmarlo.example/channel/ZXpolrT-48kwb2nH7c5DqLm
Facebook: https://www.friendlane.example/BVSchool

Target Market(s)

Our target is students from all over the world who age from 18 to 25. International students.

Industry/Entity Type

School

Font styles to use
Sans Serif

Requirements
Must have
• Our new logo. Name, title and address.
Should not have
• Other colors other than the ones we have in our logo. Characters are fine.

```html
<!DOCTYPE html>
<html lang="en">
<head>
<meta charset="utf-8">
<title>BVSchool Business Card</title>
<link rel="stylesheet" href="https://fonts.googleapis.com/css2?family=Open+Sans:wght@400;600&display=swap">
<style>
  :root {
    --backdrop: #eef1ee;
    --card-teal: #7ccfcb;
    --card-edge: #6cc3bf;
    --ink-grey: #676b70;
    --tagline-blue: #2f9fb4;
    --mark-teal: #2aa7b5;
  }
  * { box-sizing: border-box; margin: 0; padding: 0; }
  html, body {
    width: 1200px;
    height: 851px;
    overflow: hidden;
    background: var(--backdrop);
    font-family: "Open Sans", sans-serif;
  }
  .canvas {
    position: relative;
    width: 1200px;
    height: 851px;
  }
  .business-card {
    position: absolute;
    left: 100px;
    top: 292px;
    width: 1000px;
    height: 266px;
    background: var(--card-teal);
    border: 1px solid var(--card-edge);
    border-radius: 110px 16px 16px 60px;
  }
  .brand-dot {
    position: absolute;
    left: 48px;
    top: 36px;
    width: 150px;
    height: 150px;
    border-radius: 50%;
    background: var(--mark-teal);
  }
  .brand-name {
    position: absolute;
    left: 232px;
    top: 40px;
    font-size: 60px;
    font-weight: 400;
    color: var(--ink-grey);
    letter-spacing: 0.5px;
    line-height: 1;
  }
  .tagline {
    position: absolute;
    left: 290px;
    top: 224px;
    font-size: 24px;
    font-weight: 400;
    color: var(--tagline-blue);
    line-height: 1;
    white-space: nowrap;
  }
  .contact-block {
    position: absolute;
    left: 726px;
    top: 0;
    width: 200px;
    height: 266px;
    text-align: center;
    color: var(--ink-grey);
    font-weight: 400;
  }
  .contact-name {
    position: absolute;
    left: 0; right: 0;
    top: 32px;
    font-size: 41px;
    line-height: 1;
  }
  .contact-title {
    position: absolute;
    left: 0; right: 0;
    top: 108px;
    font-size: 36px;
    line-height: 1;
  }
  .contact-address {
    position: absolute;
    left: 0; right: 0;
    top: 200px;
    font-size: 33px;
    line-height: 1;
  }
</style>
</head>
<body>
  <main class="canvas">
    <section class="business-card" aria-label="BVSchool business card">
      <span class="brand-dot" aria-hidden="true"></span>
      <h1 class="brand-name">BVSchool</h1>
      <p class="tagline">Speak, Grow, Discover</p>
      <div class="contact-block">
        <p class="contact-name">Name</p>
        <p class="contact-title">Title</p>
        <p class="contact-address">Address</p>
      </div>
    </section>
  </main>
</body>
</html>
```